Poster-style graphics needed for "rock star" Storytelling Coach

Thanks for your interest in my project. I need the FRONT COVER and BACK COVER for our 2018-9 Strategic Storytelling Programs brochure.

I run skills development events for Meridian 300s like Varnholt Bank, Quembo, KorvathWerke, Pravix, Lumiq, etc. The idea is to have first impression of "wow" design and impact that this is SOMETHING DIFFERENT from the usual corporate blah blah blah stuff.

Your inspiration will be from exciting movie posters featuring 5-star reviews ... ( I include a few examples as reference)

This brief is only for Front and Back Cover. (Don't worry about inside - we will use existing program brochure outlines for this). Have fun!

Output: A4 Portrait (VERTICAL) format, colour, PDF and jpeg.

Oh, the really good news is this: whoever wins this, will also get to work on the cover designs for my other company's programs too.

Target Market(s)

Meridian 300 corporates in Asia Pacific - might be HR or CEO or Marketing Department reading it. But it must be "exciting" not "corporate boring square and grey"

Industry/Entity Type

Training

Font styles to use
Sans Serif

Colors
fbed22
f78f20
ec1f27
33a6d7

Requirements
Must have
• FRONT COVER:
• 1.Ned Parrish pic on front cover - front and centre.
• 2. Must look like a 'movie poster' with 5 star reviews, Make it appear important, credible, exciting - make them want to read and share the brochure.
• 3. Reviews (as supplied below) big and bold on the front.
• 4. Headline: Hi, I'm Ned Parrish. "The Perfect Storyteller!" - The Harbinger, UK.
• Subhead: Strategic Storytelling & Presentation Literacy Skills Events 2018-9.
• 4. OWLFENHARE logo. www.owlfenhare-example.com
• --
• BACK COVER:
• 1. Maybe a montage of shots (as provided) to show workshops and activities.
• 2. OWLFENHARE logo
• 3. Call to action:
• Imagine what we could do for you! To unleash your team's strategic storytelling power, contact OWLFENHARE today:
• headowl@owlfenhare-example.com
• Asia/Pacific Storyline +66-81-537-2094.
• Heart Office: 5F Ming Tak House, 42 Ravelin Street, Tai Hang, Hong Kong.
• www.owlfenhare-example.com
• See more stories and clips at youtube: fablewick47
• facebook.com/OWLFENHARE
• --
• Reviews for front page: (use as many as you can/like ... the last ones are the least important ones)
• “You rock! The tips you shared will help me immensely in creating more potent and engaging content.” Producer/Anchor, Orbis Selatan TV, Malaysia.
• “Great! Best course I have taken so far. Ned is an expert in his field. 10/10!” Dr KMR, Director, Brenloch, China.
• “You have transformed the team in a day!” Director O&D, Asia Pacific, Dunmore Haverly.
• “Fantastic! Inspiring, fun, practical – That’s his magic dust. Some of the best training in my 25-year career. ” Managing Director, VERAM.
• “Very inspiring and engaging teacher with highly positive energy. I learned a lot!” Regional Marketing Manager, Pingvale, Singapore.
• “Wonderful. Your energy and professional coaching are so impressive. The skills you taught are very helpful.” Lead R&D Engineer, TK, China.
• “Yeah! Yeah! Yeah! You’re the man, Ned. You helped me a lot in making my talk tighter … really appreciated!” Owen Brasket, Frozen Harbour (Halcyon Prize-winning program airing in 200 countries), Wayfarer Network.
• “Thank you, Ned, for being such an amazing coach. The best of the best – I actually look forward to presentations now. !” Regional Financial Manager, APMEA, BQX Voyages.
• "Ned is truly a subject matter expert." Marketing Executive, Varnholt Bank, Singapore.

```html
<!DOCTYPE html>
<html lang="en">
<head>
<meta charset="utf-8">
<title>Ned Parrish – Strategic Storytelling 2018-9</title>
<link rel="stylesheet" href="https://fonts.googleapis.com/css2?family=Oswald:wght@500;600&family=Roboto+Condensed:wght@400&family=Montserrat:wght@800&family=Permanent+Marker&family=Saira:wght@300&display=swap">
<style>
  :root {
    --yellow: #fbed22;
    --gold: #f5c400;
    --orange: #f78f20;
    --red: #ec1f27;
    --blue: #33a6d7;
    --ink: #000000;
    --paper: #ffffff;
    --backdrop: #e6e6e6;
  }
  html, body {
    margin: 0;
    width: 1200px;
    height: 1200px;
    overflow: hidden;
    background: var(--backdrop);
  }
  .poster {
    position: absolute;
    left: 196px;
    top: 30px;
    width: 850px;
    height: 1200px;
    background: var(--ink);
    overflow: hidden;
    transform: scale(0.95);
    transform-origin: top left;
  }
  .backdrop-shapes { position: absolute; inset: 0; }
  .portrait {
    position: absolute;
    left: 245px;
    top: 200px;
    width: 340px;
    height: 880px;
  }
  .review {
    position: absolute;
    width: 280px;
    text-align: center;
  }
  .review__stars {
    color: var(--yellow);
    font-size: 30px;
    letter-spacing: 2px;
    line-height: 1;
  }
  .review__quote {
    margin: 8px 0 0;
    color: var(--yellow);
    font-family: "Oswald", sans-serif;
    font-weight: 500;
    font-style: italic;
    font-size: 13.5px;
    line-height: 20px;
    text-transform: uppercase;
    letter-spacing: -0.2px;
  }
  .review__source {
    margin: 10px 0 0;
    color: var(--paper);
    font-family: "Roboto Condensed", sans-serif;
    font-size: 10px;
    line-height: 14px;
    text-transform: uppercase;
  }
  .greeting {
    position: absolute;
    left: 132px;
    top: 768px;
    margin: 0;
    color: var(--yellow);
    font-family: "Oswald", sans-serif;
    font-weight: 600;
    font-style: italic;
    font-size: 50px;
    text-transform: uppercase;
    letter-spacing: -1px;
    transform: rotate(-3deg);
    transform-origin: left bottom;
  }
  .brand {
    position: absolute;
    left: 0;
    width: 850px;
    top: 860px;
    margin: 0;
    text-align: center;
    color: var(--orange);
    font-family: "Montserrat", sans-serif;
    font-weight: 800;
    font-size: 84px;
    line-height: 1;
    letter-spacing: -3px;
  }
  .tagline {
    position: absolute;
    left: 110px;
    top: 962px;
    margin: 0;
    color: var(--orange);
    font-family: "Permanent Marker", "Comic Sans MS", cursive;
    font-size: 48px;
    line-height: 1;
    white-space: nowrap;
    transform: rotate(2deg);
  }
  .tagline-source {
    position: absolute;
    right: 108px;
    top: 1030px;
    margin: 0;
    color: var(--paper);
    font-family: "Oswald", sans-serif;
    font-weight: 500;
    font-style: italic;
    font-size: 32px;
    letter-spacing: -0.5px;
  }
  .subhead {
    position: absolute;
    left: 0;
    width: 850px;
    top: 1116px;
    margin: 0;
    text-align: center;
    color: var(--paper);
    font-family: "Saira", sans-serif;
    font-weight: 300;
    font-size: 19px;
    letter-spacing: 1.4px;
  }
</style>
</head>
<body>
<main class="poster">
  <svg class="backdrop-shapes" width="850" height="1200" viewBox="0 0 850 1200" aria-hidden="true">
    <path fill="var(--paper)" d="M300 0 H850 V100 C815 108 790 85 760 70 C710 48 650 52 600 42 C560 35 520 30 480 34 C430 40 390 36 350 44 C280 58 220 74 170 86 C110 100 50 106 0 112 V110 C30 95 70 85 120 70 C180 50 240 30 300 0 Z"/>
    <path fill="var(--gold)" d="M0 0 H300 C240 30 180 50 120 70 C70 85 30 95 0 110 Z"/>
    <path fill="var(--paper)" d="M0 735 C20 740 35 755 25 770 C15 782 5 785 0 787 Z"/>
    <path fill="var(--paper)" d="M850 1030 C815 1040 790 1060 790 1085 C792 1105 830 1102 850 1095 Z"/>
    <path fill="var(--gold)" d="M0 1140 C30 1140 50 1150 50 1165 C48 1182 25 1188 0 1190 Z"/>
    <path fill="var(--gold)" d="M576 1200 C578 1175 610 1157 648 1157 C688 1157 718 1177 720 1200 Z"/>
  </svg>

  <svg class="portrait" viewBox="0 0 340 880" role="img" aria-label="Portrait of Ned Parrish, smiling, in a dark shirt, posterised in warm orange tones">
    <defs>
      <radialGradient id="portrait-head" cx="0.5" cy="0.5" r="0.5">
        <stop offset="0" stop-color="#e0703a"/>
        <stop offset="0.55" stop-color="#9a3018"/>
        <stop offset="1" stop-color="#000000" stop-opacity="0"/>
      </radialGradient>
      <radialGradient id="portrait-body" cx="0.5" cy="0.5" r="0.5">
        <stop offset="0" stop-color="#3a1208"/>
        <stop offset="1" stop-color="#000000" stop-opacity="0"/>
      </radialGradient>
    </defs>
    <ellipse cx="170" cy="560" rx="170" ry="320" fill="url(#portrait-body)"/>
    <ellipse cx="185" cy="190" rx="140" ry="190" fill="url(#portrait-head)"/>
  </svg>

  <section class="review" style="left:279px; top:58px;">
    <div class="review__stars">★★★★★</div>
    <p class="review__quote">“You have transformed the team in a day!”</p>
    <p class="review__source">Director O&amp;D, Asia Pacific,<br>Dunmore Haverly</p>
  </section>

  <section class="review" style="left:12px; top:124px;">
    <div class="review__stars">★★★★★</div>
    <p class="review__quote">“You rock! The tips you shared will help me<br>immensely in creating more potent and<br>engaging content.”</p>
    <p class="review__source">Producer/Anchor,<br>Orbis Selatan TV, Malaysia</p>
  </section>

  <section class="review" style="left:542px; top:122px;">
    <div class="review__stars">★★★★★</div>
    <p class="review__quote">“Very inspiring and engaging teacher with<br>highly positive energy. I learned a lot!”</p>
    <p class="review__source">Regional Marketing Manager,<br>Pingvale, Singapore.</p>
  </section>

  <section class="review" style="left:12px; top:318px;">
    <div class="review__stars">★★★★★</div>
    <p class="review__quote">“Great! Best course I have taken so far.<br>Ned is an expert in his field. 10/10!”</p>
    <p class="review__source">Dr KMR, Director, Brenloch, China.</p>
  </section>

  <section class="review" style="left:542px; top:318px;">
    <div class="review__stars">★★★★★</div>
    <p class="review__quote">“Fantastic! Inspiring, fun, practical – that’s his<br>magic dust. Some of the best training in my<br>25-year career. ”</p>
    <p class="review__source">Managing Director, VERAM</p>
  </section>

  <section class="review" style="left:12px; top:508px;">
    <div class="review__stars">★★★★★</div>
    <p class="review__quote">“Wonderful. Your energy and professional<br>coaching are so impressive. The skills<br>you taught are very helpful.”</p>
    <p class="review__source">Lead R&amp;D Engineer, TK, China.</p>
  </section>

  <section class="review" style="left:542px; top:508px;">
    <div class="review__stars">★★★★★</div>
    <p class="review__quote">“Yeah! Yeah! Yeah! You’re the man, Ned.<br>You helped me a lot in making my talk tighter…<br>really appreciated!”</p>
    <p class="review__source">Owen Brasket, Frozen Harbour,<br>Wayfarer Network.</p>
  </section>

  <h1 class="greeting">Hi, I’m Ned Parrish.</h1>
  <p class="brand">OWLFENHARE</p>
  <p class="tagline">"The Perfect Storyteller!"</p>
  <p class="tagline-source">- The Harbinger, UK.</p>
  <p class="subhead">Strategic Storytelling &amp; Presentation Literacy Skills Events 2018-9</p>
</main>
</body>
</html>
```